Zielgruppe
Was machen wir: Datenschutz und Informationssicherheit als Dienstleistung.
Zielgruppe: Mittelständische Unternehmenskunden 500 -5000 Mitarbeiter
Aufgabenstellung
Wir benötigen eine neue Powerpoint Vorlage. Die alte Vorlage ist nicht mehr zeitgemäß.
Format: DIN 16:9
Standardschriftart: Calibri
Zielgruppe: Mittleres und gehobenes Management
CI: Unsere Farben können auf unserer Webseite eingesehen werden.

```html
<!DOCTYPE html>
<html lang="de">
<head>
<meta charset="utf-8">
<title>Agenda</title>
<link rel="stylesheet" href="https://fonts.googleapis.com/css2?family=Carlito:wght@400;700&family=Open+Sans:wght@300&display=swap">
<style>
  :root {
    --slide-blue: #3f4e86;
    --streak-light: #5a6aa8;
    --accent-orange: #ff8200;
    --text-white: #ffffff;
    --logo-grey: #c9ccd8;
  }
  html, body {
    margin: 0;
    padding: 0;
    width: 1200px;
    height: 675px;
    overflow: hidden;
    background: var(--slide-blue);
  }
  .slide {
    position: relative;
    width: 1200px;
    height: 675px;
    overflow: hidden;
    background: var(--slide-blue);
    font-family: "Carlito", "Calibri", sans-serif;
    color: var(--text-white);
  }
  .backdrop {
    position: absolute;
    inset: 0;
    background:
      linear-gradient(176deg, transparent 30%, rgba(110,125,190,0.35) 34%, transparent 38%),
      linear-gradient(182deg, transparent 44%, rgba(100,115,180,0.25) 47%, transparent 58%),
      linear-gradient(160deg, transparent 70%, rgba(70,120,180,0.35) 78%, transparent 86%),
      linear-gradient(170deg, rgba(120,100,190,0.35) 0%, transparent 10%),
      var(--slide-blue);
  }
  .edge {
    position: absolute;
    top: 0;
    width: 12.5px;
    height: 675px;
    background: var(--accent-orange);
  }
  .edge--left { left: 0; }
  .edge--right { right: 0; }
  .title {
    position: absolute;
    left: 61px;
    top: 34px;
    margin: 0;
    font-weight: 700;
    font-size: 52px;
    line-height: 1;
    letter-spacing: 9px;
    color: var(--accent-orange);
  }
  .title-rule {
    position: absolute;
    left: 12.5px;
    top: 91.5px;
    width: 290px;
    height: 2px;
    background: var(--accent-orange);
  }
  .agenda-item {
    position: absolute;
    width: 500px;
    height: 100px;
  }
  .item-number {
    position: absolute;
    left: 0;
    top: 0;
    width: 96px;
    height: 96px;
    border: 2px solid var(--accent-orange);
    border-radius: 50%;
    display: flex;
    align-items: center;
    justify-content: center;
    font-family: "Open Sans", sans-serif;
    font-weight: 300;
    font-size: 46px;
    letter-spacing: 6px;
    padding-left: 6px;
    box-sizing: content-box;
    width: 92px;
    color: var(--accent-orange);
  }
  .item-text {
    position: absolute;
    left: 129px;
    top: 3px;
    font-size: 23px;
    line-height: 31px;
  }
  .item-heading {
    display: block;
    font-weight: 700;
  }
  .brand {
    position: absolute;
    right: 48px;
    bottom: 26px;
    font-size: 18px;
    font-weight: 700;
    color: var(--logo-grey);
  }
</style>
</head>
<body>
<main class="slide">
  <div class="backdrop" role="img" aria-label="Abstrakter blauer Hintergrund mit hellen Lichtstreifen"></div>
  <div class="edge edge--left"></div>
  <div class="edge edge--right"></div>

  <h1 class="title">AGENDA</h1>
  <div class="title-rule"></div>

  <section class="agenda-item" style="left:62px; top:152px;">
    <div class="item-number">01</div>
    <p class="item-text" style="margin:0"><span class="item-heading">LOREM IPSUM</span>Lorem ipsum dolor sit<br>amet, consectetur</p>
  </section>
  <section class="agenda-item" style="left:601px; top:152px;">
    <div class="item-number">02</div>
    <p class="item-text" style="margin:0"><span class="item-heading">LOREM IPSUM</span>Lorem ipsum dolor sit<br>amet, consectetur</p>
  </section>
  <section class="agenda-item" style="left:62px; top:313px;">
    <div class="item-number">03</div>
    <p class="item-text" style="margin:0"><span class="item-heading">LOREM IPSUM</span>Lorem ipsum dolor sit<br>amet, consectetur</p>
  </section>
  <section class="agenda-item" style="left:601px; top:313px;">
    <div class="item-number">04</div>
    <p class="item-text" style="margin:0"><span class="item-heading">LOREM IPSUM</span>Lorem ipsum dolor sit<br>amet, consectetur</p>
  </section>
  <section class="agenda-item" style="left:62px; top:473px;">
    <div class="item-number">05</div>
    <p class="item-text" style="margin:0"><span class="item-heading">LOREM IPSUM</span>Lorem ipsum dolor sit<br>amet, consectetur</p>
  </section>
  <section class="agenda-item" style="left:601px; top:473px;">
    <div class="item-number">06</div>
    <p class="item-text" style="margin:0"><span class="item-heading">LOREM IPSUM</span>Lorem ipsum dolor sit<br>amet, consectetur</p>
  </section>

  <div class="brand">Norveda</div>
</main>
</body>
</html>
```